Manufacturing Company needs a print add design

We need a print ad that communicates the benefits of delivering a vaccine through an inhaler.
Given the nature of the pharmaceutical market, use of real people pictures is disencouraged, but drawings/cartoons or schemes are ok, although with constraints. We would like to see designs that are raceless and address medically supervised delivery.
The photos provided can serve as inspiration, but may not be used directly on the final design.
The final design should communicate convenience, ease of use and limited refrigeration requirements, specially relevant for emerging markets.

Target Market(s)

Vaccine delivery / pharmaceutical market

Industry/Entity Type

Pharmaceutical

Requirements
Should not have
• The print add design should not have real people photographs.

```html
<!DOCTYPE html>
<html lang="en">
<head>
<meta charset="utf-8">
<title>Easier vaccination process</title>
<link href="https://fonts.googleapis.com/css2?family=Roboto:wght@300;400&display=swap" rel="stylesheet">
<style>
  :root {
    --bg-light: #fafafa;
    --bg-mid: #e4e4e4;
    --bg-edge: #d2d2d2;
    --card: #f6f6f6;
    --card-lower: #fbfbfb;
    --red: #e8473f;
    --teal: #37b2bc;
    --teal-soft: #9fdbe0;
    --teal-pale: #d5f0f2;
    --green: #3fd7a2;
    --grey-text: #8a8a8a;
  }
  * { margin: 0; padding: 0; box-sizing: border-box; }
  html, body { width: 1200px; height: 849px; overflow: hidden; }
  body {
    position: relative;
    font-family: "Roboto", Arial, sans-serif;
    font-weight: 300;
    background: radial-gradient(ellipse 55% 60% at 70% 48%, var(--bg-light) 0%, var(--bg-mid) 60%, var(--bg-edge) 100%);
  }
  .headline {
    position: absolute; left: 643px; top: 104px;
    font-size: 44px; font-weight: 300; color: var(--teal); letter-spacing: 0.3px;
    white-space: nowrap;
  }
  .comparison-card {
    position: absolute; left: 71px; top: 109px; width: 525px; height: 602px;
    background: var(--card);
    border-radius: 34px;
    border-top: 3px solid var(--red);
    overflow: hidden;
    box-shadow: 0 1px 3px rgba(0,0,0,0.06);
  }
  .method {
    position: absolute; left: 0; width: 100%;
  }
  .method--injection { top: 0; height: 300px; }
  .method--inhaler {
    top: 296px; height: 310px;
    background: var(--card-lower);
    border-top: 3px solid var(--teal);
    border-radius: 34px 34px 0 0;
  }
  .method-icon {
    position: absolute; border-radius: 6px;
  }
  .method--injection .method-icon {
    left: 146px; top: 44px; width: 70px; height: 66px;
    background: linear-gradient(135deg, transparent 40%, var(--red) 40%, var(--red) 60%, transparent 60%);
  }
  .method--inhaler .method-icon {
    left: 162px; top: 26px; width: 40px; height: 68px;
    background: var(--teal-soft);
  }
  .method-kicker {
    position: absolute; left: 217px; font-size: 19px; color: var(--grey-text); white-space: nowrap;
  }
  .method--injection .method-kicker { top: 50px; }
  .method--inhaler .method-kicker { top: 28px; }
  .method-name { position: absolute; white-space: nowrap; }
  .method--injection .method-name {
    left: 222px; top: 70px; font-size: 35px; font-weight: 400; color: var(--red);
  }
  .method--inhaler .method-name {
    left: 214px; top: 46px; font-size: 51px; font-weight: 300; color: var(--teal);
  }
  .feature {
    position: absolute; width: 160px; margin-left: -80px; text-align: center;
    font-size: 16px; line-height: 21px;
  }
  .method--injection .feature { top: 146px; color: var(--red); }
  .method--inhaler .feature { top: 150px; color: var(--teal); }
  .feature svg, .feature .feature-art { display: block; margin: 14px auto 0; }
  .feature-art {
    width: 56px; height: 62px; border-radius: 28px 28px 10px 10px;
    background: var(--teal-pale);
  }
  .figure-art {
    position: absolute; left: 768px; top: 212px; width: 282px; height: 530px;
    border-radius: 120px 120px 40px 40px;
    background: linear-gradient(180deg, var(--teal-soft) 0%, var(--teal-pale) 60%, rgba(255,255,255,0.2) 100%);
  }
</style>
</head>
<body>
  <h1 class="headline">Easier vaccination process</h1>

  <section class="comparison-card">
    <div class="method method--injection">
      <div class="method-icon" role="img" aria-label="Syringe icon"></div>
      <p class="method-kicker">Vaccination by</p>
      <h2 class="method-name">injection</h2>

      <div class="feature" style="left:89px">Infections<br>threats
        <svg width="96" height="40" viewBox="0 0 96 40"><polyline points="2,24 20,24 28,10 36,34 44,14 52,30 60,20 68,24 94,24" fill="none" stroke="var(--red)" stroke-width="2.4" stroke-linejoin="round"/></svg>
      </div>
      <div class="feature" style="left:258px">Medical<br>assistance
        <svg width="40" height="40" viewBox="0 0 40 40"><rect x="15" y="6" width="10" height="30" fill="var(--red)"/><rect x="5" y="16" width="30" height="10" fill="var(--red)"/></svg>
      </div>
      <div class="feature" style="left:432px">refrigeration<br>requirements
        <svg width="24" height="72" viewBox="0 0 24 72"><rect x="8.5" y="2" width="7" height="56" rx="3.5" fill="var(--red)"/><circle cx="12" cy="62" r="8" fill="var(--red)"/></svg>
      </div>
    </div>

    <div class="method method--inhaler">
      <div class="method-icon" role="img" aria-label="Inhaler icon"></div>
      <p class="method-kicker">Vaccination by</p>
      <h2 class="method-name">Inhaler</h2>

      <div class="feature" style="left:89px">No Infections<br>threats
        <svg width="36" height="30" viewBox="0 0 36 30"><polyline points="4,15 13,24 32,5" fill="none" stroke="var(--green)" stroke-width="6" stroke-linecap="round" stroke-linejoin="round"/></svg>
      </div>
      <div class="feature" style="left:258px">Easy to use
        <div class="feature-art" role="img" aria-label="Small outline of a head inhaling"></div>
      </div>
      <div class="feature" style="left:432px">Limited refrigeration<br>requirements
        <svg width="24" height="72" viewBox="0 0 24 72"><rect x="8.5" y="2" width="7" height="56" rx="3.5" fill="var(--green)"/><circle cx="12" cy="62" r="8" fill="var(--green)"/></svg>
      </div>
    </div>
  </section>

  <div class="figure-art" role="img" aria-label="Translucent teal silhouette of a person in profile using an inhaler, with bubbles travelling down the airway into the lungs"></div>
</body>
</html>
```